Business Card Design

I'm a young beekeeper (22 years old) just starting out. I own and run 80 hives and would like to eventually build up to 1000. My aim is to run it in tandem with our family farm that is currently running sheep and beef. Unlike a number of honey companies on the East Coast (or the North Island, NZ) I am local and will expand onto the lease blocks that our family is also leasing. I want a simple plain logo/photo. The designer may wish to use one of the photos as a background outline or however they chose. The mountain is Aorangi and our farm borders one side of it.

Target Market(s)

From local land owners to wholesale honey buyers

Industry/Entity Type

Farm

Contact Information for Business Card

Pekeriu Honey
Manager Owner Manaia Brooks
email pekeriuhoney@tuimailbox.co.nz
mobile 0217394461

Requirements
Must have
• The details submitted. The brand Pekeriu Honey to be the main feature. The other details can be smaller.
Should not have
• Must not include a picture of a bee or hive. Use a modern font. Don't use koru but may incorporate poutama.

```html
<!DOCTYPE html>
<html lang="en">
<head>
<meta charset="utf-8">
<title>Pekeriu Honey – Business Card</title>
<link rel="stylesheet" href="https://fonts.googleapis.com/css2?family=Cinzel:wght@400;600&family=Open+Sans:wght@400;700&display=swap">
<style>
  :root {
    --stage: #d9d9d9;
    --card-white: #fbfbfa;
    --honey-light: #fbd36a;
    --honey: #f4b52a;
    --honey-deep: #e59a17;
    --brand-gold: #f2b52b;
    --text-light: #ffffff;
    --sky: #e4edf3;
    --sky-blue: #a9c8dc;
    --ridge: #2f4a46;
    --ridge-mid: #3f5d57;
    --slope: #6f6a48;
  }
  * { box-sizing: border-box; margin: 0; padding: 0; }
  html, body {
    width: 1200px; height: 1023px; overflow: hidden;
    background: var(--stage);
  }
  .canvas {
    position: relative; width: 1200px; height: 1023px;
    display: flex; flex-direction: column; align-items: center; justify-content: center; gap: 70px;
  }
  .card {
    position: relative; width: 640px; height: 356px; overflow: hidden;
    box-shadow: 0 8px 24px rgba(0,0,0,.25);
  }

  /* Front */
  .card--front { background: var(--card-white); display: flex; }
  .brand-side {
    width: 320px; height: 100%;
    display: flex; flex-direction: column; align-items: center; justify-content: center; gap: 22px;
  }
  .brand-dot {
    width: 70px; height: 70px; border-radius: 50%;
    background: var(--brand-gold);
  }
  .brand-name {
    font-family: "Cinzel", serif; font-weight: 400;
    font-size: 32px; letter-spacing: 1px; color: var(--brand-gold);
    white-space: nowrap;
  }
  .divider-line { width: 4px; height: 100%; background: var(--honey); }
  .divider-gap { width: 10px; height: 100%; background: var(--card-white); }
  .details-side {
    flex: 1; height: 100%;
    background: linear-gradient(90deg, var(--honey-light) 0%, var(--honey) 55%, var(--honey-deep) 100%);
    color: var(--text-light);
    font-family: "Open Sans", sans-serif;
    padding: 118px 0 0 44px;
  }
  .contact-name { font-weight: 700; font-size: 20px; line-height: 1.2; }
  .contact-role { font-size: 13px; margin-top: 2px; }
  .contact-lines { margin-top: 42px; font-size: 13px; line-height: 1.9; white-space: nowrap; }

  /* Back */
  .card--back { display: flex; align-items: center; justify-content: center; }
  .landscape {
    position: absolute; inset: 0;
    background:
      linear-gradient(20deg, rgba(111,106,72,.55) 0%, rgba(111,106,72,0) 35%),
      linear-gradient(115deg, var(--ridge) 0%, var(--ridge-mid) 40%, var(--sky-blue) 62%, var(--sky) 85%, #ffffff 100%);
  }
  .back-brand {
    position: relative;
    font-family: "Cinzel", serif; font-weight: 400;
    font-size: 46px; letter-spacing: 2px; color: var(--brand-gold);
    white-space: nowrap;
  }
</style>
</head>
<body>
  <main class="canvas">
    <section class="card card--front" aria-label="Business card front">
      <div class="brand-side">
        <span class="brand-dot" aria-hidden="true"></span>
        <span class="brand-name">Pekeriu Honey</span>
      </div>
      <div class="divider-gap"></div>
      <div class="divider-line"></div>
      <div class="divider-gap"></div>
      <div class="details-side">
        <p class="contact-name">Manaia Brooks</p>
        <p class="contact-role">Manager Owner</p>
        <div class="contact-lines">
          <p>M: 0217394461</p>
          <p>E: pekeriuhoney@tuimailbox.co.nz</p>
        </div>
      </div>
    </section>

    <section class="card card--back" aria-label="Business card back">
      <div class="landscape" role="img" aria-label="Photograph of the mountain and forested valley beneath a bright sky"></div>
      <span class="back-brand">Pekeriu Honey</span>
    </section>
  </main>
</body>
</html>
```